Business card Zottelgarten

Business card is for a self-employed dog trainer with own dog school. Name and logo of the dog school are available. Color specifications as well. The design should be classy and minimalist, but also modern. An already existing idea would be: Front: Only the logo Back: Contact data

Font styles to use
Serif
Sans Serif
Other font styles liked:
• Trajan Pro

Colors
f78f20

Requirements
Must have
• Name: Margit Wendler-Rasch Title: Dipl. Dog Trainer Contain my logo Follow my font and color preferences (see files)

```html
<!DOCTYPE html>
<html lang="en">
<head>
<meta charset="utf-8">
<title>Zottelgarten – Business Card</title>
<link rel="stylesheet" href="https://fonts.googleapis.com/css2?family=Cinzel:wght@400;500&display=swap">
<style>
  :root {
    --backdrop: #b4b4b6;
    --brand-orange: #f78f20;
    --deep-brown: #7a4f2c;
    --warm-amber: #e08a2c;
    --light-orange: #fbb04a;
    --paper: #f2f2f2;
    --band-grey: #e6e6e6;
    --ink-grey: #6b6460;
    --ink-dark: #4a3a2c;
    --gold: #f6e51c;
  }
  * { margin: 0; padding: 0; box-sizing: border-box; }
  html, body { width: 1200px; height: 872px; overflow: hidden; }
  body {
    background: var(--backdrop);
    font-family: "Cinzel", serif;
    position: relative;
  }
  .card {
    position: absolute;
    top: 141px;
    width: 340px;
    height: 590px;
    overflow: hidden;
    box-shadow: 0 10px 30px rgba(0,0,0,0.18);
  }
  /* Front */
  .card--front {
    left: 200px;
    background: linear-gradient(225deg, var(--brand-orange) 0%, var(--warm-amber) 35%, var(--deep-brown) 100%);
  }
  .brand-mark {
    position: absolute;
    left: 0; right: 0;
    top: 150px;
    display: flex;
    flex-direction: column;
    align-items: center;
    gap: 14px;
    color: rgba(255, 200, 110, 0.28);
  }
  .brand-mark__circle {
    width: 130px; height: 130px;
    border-radius: 50%;
    background: rgba(255, 200, 110, 0.18);
  }
  .brand-mark__name {
    font-size: 30px;
    font-weight: 400;
    letter-spacing: 2px;
  }
  .brand-mark__web {
    font-size: 8px;
    letter-spacing: 4px;
    margin-top: -10px;
  }
  .front-band {
    position: absolute;
    left: 0; right: 0; bottom: 0;
    height: 175px;
    background: var(--band-grey);
  }
  .front-band__title {
    position: absolute;
    right: 28px;
    top: 48px;
    font-size: 32px;
    color: var(--brand-orange);
    letter-spacing: 1px;
  }
  .front-band__stripe {
    position: absolute;
    left: 0; right: 0;
    height: 12px;
    background: linear-gradient(90deg, var(--deep-brown) 0%, var(--warm-amber) 30%, var(--gold) 55%, var(--brand-orange) 80%, var(--brand-orange) 100%);
  }
  .front-band__stripe--upper { top: 108px; }
  .front-band__stripe--lower { top: 126px; }

  /* Back */
  .card--back {
    left: 660px;
    background: linear-gradient(90deg, var(--light-orange) 0%, var(--brand-orange) 25%, #f9b061 50%, #f6dcbd 72%, var(--paper) 85%, var(--paper) 100%);
  }
  .contact {
    position: absolute;
    left: 34px;
    top: 62px;
    display: grid;
    grid-template-columns: 64px auto;
    row-gap: 16px;
    color: var(--ink-dark);
  }
  .contact__label { font-size: 11px; letter-spacing: 1px; }
  .contact__value { font-size: 13px; }
  .contact__value--title { font-size: 11px; }
  .card--back .brand-mark {
    top: 170px;
    color: rgba(255, 210, 140, 0.45);
  }
  .card--back .brand-mark__circle { background: rgba(255, 220, 160, 0.25); }
  .back-title {
    position: absolute;
    left: 0; right: 0;
    bottom: 70px;
    text-align: center;
    font-size: 34px;
    color: var(--ink-grey);
    letter-spacing: 1px;
  }
</style>
</head>
<body>
  <section class="card card--front">
    <div class="brand-mark">
      <div class="brand-mark__circle"></div>
      <div class="brand-mark__name">ZOTTELGARTEN</div>
      <div class="brand-mark__web">WWW.ZOTTELGARTEN.CH</div>
    </div>
    <div class="front-band">
      <div class="front-band__title">DOG TRAINER</div>
      <div class="front-band__stripe front-band__stripe--upper"></div>
      <div class="front-band__stripe front-band__stripe--lower"></div>
    </div>
  </section>

  <section class="card card--back">
    <div class="contact">
      <span class="contact__label">NAME :</span>
      <span class="contact__value">Margit Wendler-Rasch</span>
      <span class="contact__label">TITLE :</span>
      <span class="contact__value contact__value--title">DIPL. DOG TRAINER</span>
    </div>
    <div class="brand-mark">
      <div class="brand-mark__circle"></div>
      <div class="brand-mark__name">ZOTTELGARTEN</div>
      <div class="brand-mark__web">WWW.ZOTTELGARTEN.CH</div>
    </div>
    <div class="back-title">DOG TRAINER</div>
  </section>
</body>
</html>
```